Plimbo.com re-design on Wix platform

Re-do this website : www.plimbo.com
Plimbo is a sound conditioner that uses the calming, sedative qualities of mundane rhythmic stimulation to allow its users to rest easier and deeper than they normally would.
I think of Plimbo.com as a web app; a place to use and buy the product. Im open to suggestion on site layouts, whether you use one page or several.
Use the same color scheme: purple, white, black, grey/silver
I would like a place for testimonials, even though you don't currently see one on the site. Other than that, assume the content will stay mostly the same.
I'd like a clean, modern, professional look. The site will reside on Wix platform.

```html
<!DOCTYPE html>
<html lang="en">
<head>
<meta charset="utf-8">
<title>Plimbo – sound conditioner</title>
<link href="https://fonts.googleapis.com/css2?family=Russo+One&family=Open+Sans:ital,wght@0,400;0,600;0,700;1,400&display=swap" rel="stylesheet">
<style>
:root{
  --purple:#a30fb4;
  --purple-deep:#8a0a99;
  --purple-soft:#c25bd0;
  --ink:#111111;
  --dark:#1c1c1c;
  --grey:#e9ecee;
  --silver:#b9bcc0;
  --text:#555a5f;
  --white:#ffffff;
}
*{box-sizing:border-box;margin:0;padding:0}
html,body{width:1200px;height:4018px;overflow:hidden}
body{font-family:"Open Sans",Arial,sans-serif;color:var(--text);background:var(--white);position:relative}
.heading{font-family:"Russo One","Arial Black",sans-serif;text-transform:uppercase;color:var(--ink)}
.brand{font-family:"Open Sans",Arial,sans-serif;font-weight:700;color:var(--purple);display:flex;align-items:center;gap:10px}
.brand-dot{width:14px;height:14px;background:var(--purple)}
.social{display:flex;gap:10px}
.social span{width:14px;height:14px;border-radius:50%;background:currentColor;display:block}

/* hero */
.hero{position:absolute;top:0;left:0;width:1200px;height:798px;overflow:hidden}
.hero-photo{position:absolute;inset:0;background:linear-gradient(180deg,#6b4e78 0%,#5b3f69 35%,#7d6b8a 65%,#4a3556 100%)}
.hero-photo::after{content:"";position:absolute;inset:0;background:rgba(95,30,110,.35)}
.hero .brand{position:absolute;top:10px;left:50%;transform:translateX(-50%);font-size:72px;color:var(--white)}
.hero .brand .brand-dot{background:var(--white);width:20px;height:20px}
.hero .social{position:absolute;top:14px;left:904px;color:var(--white)}
.hero-copy{position:absolute;top:262px;left:260px;width:680px;text-align:center;color:#f1e9f3;font-size:19px;line-height:27px}
.hero-copy em{font-style:normal;color:var(--purple-soft)}
.play{position:absolute;top:430px;left:530px;width:140px;height:140px;border:2px solid rgba(255,255,255,.6);border-radius:50%;background:rgba(255,255,255,.1)}
.play svg{position:absolute;left:52px;top:44px}
.dots{position:absolute;top:728px;left:550px;display:flex;gap:8px}
.dots span{width:12px;height:12px;border-radius:50%;border:1.5px solid rgba(255,255,255,.8)}
.dots span.on{background:rgba(255,255,255,.8)}

/* nav */
.nav{position:absolute;top:798px;left:0;width:1200px;height:81px;background:var(--white);border-bottom:1px solid #eee;display:flex;align-items:center;padding:0 76px}
.nav .brand{font-size:40px}
.nav ul{list-style:none;display:flex;gap:36px;margin-left:auto;margin-right:60px;font-size:12px;font-weight:600;color:var(--ink)}
.nav li.active{color:var(--purple)}
.nav .social{color:var(--purple)}

/* how it works */
.how{position:absolute;top:879px;left:0;width:1200px;height:581px}
.how-text{position:absolute;top:130px;left:100px;width:380px}
.how-text h2{font-size:34px}
.how-text p{font-size:11px;line-height:16px;margin-top:12px}
.how-text .lead{color:var(--purple);font-weight:600;margin-top:28px}
.how-photo{position:absolute;top:86px;left:580px;width:508px;height:386px;border-radius:4px;background:linear-gradient(135deg,#e6e4e0,#c9c7c3 55%,#8e9297)}

/* benefits */
.benefits{position:absolute;top:1460px;left:0;width:1200px;height:598px;background:var(--purple)}
.benefits h2{color:var(--white);text-align:center;font-size:30px;margin-top:20px}
.grid{position:absolute;top:96px;left:72px;display:grid;grid-template-columns:repeat(7,132px);row-gap:34px;column-gap:20px}
.bubble{width:132px;height:132px;border-radius:50%;position:relative;border:3px solid var(--white);overflow:hidden;background:linear-gradient(160deg,#cfc7c0,#6f6670)}
.bubble.warm{background:linear-gradient(160deg,#f2c23d,#c2362e)}
.bubble.dim{background:linear-gradient(160deg,#7c6c84,#3c2d44)}
.bubble.mono{background:linear-gradient(160deg,#c7c7c7,#3d3d3d)}
.bubble b{position:absolute;left:0;right:0;bottom:22px;background:rgba(163,15,180,.85);color:var(--white);font-size:9px;font-weight:600;text-align:center;line-height:15px}

/* download */
.download{position:absolute;top:2058px;left:0;width:1200px;height:334px;background:linear-gradient(180deg,#2b2b2b,#1a1a1a);text-align:center;color:var(--white)}
.download h2{color:var(--white);font-size:38px;margin-top:76px}
.download p{font-size:17px;margin-top:6px;color:#ddd}
.download .btn{display:inline-block;margin-top:30px;width:326px;height:76px;line-height:74px;border:2px solid var(--white);border-radius:4px;font-weight:700;font-size:15px;letter-spacing:1px}

/* expect */
.expect{position:absolute;top:2392px;left:0;width:1200px;height:536px}
.expect-photo{position:absolute;top:72px;left:122px;width:452px;height:356px;background:linear-gradient(135deg,#dcd8d2,#b5aea5 60%,#8c8378)}
.expect-text{position:absolute;top:130px;left:688px;width:388px;text-align:right}
.expect-text h2{font-size:28px}
.expect-text p{font-size:10.5px;line-height:27px;margin-top:20px}
.expect-text .btn{display:inline-block;margin-top:18px;width:116px;height:46px;line-height:46px;background:var(--ink);color:var(--white);font-size:11px;font-weight:600;text-align:center;border-radius:4px}

/* testimonials */
.testimonials{position:absolute;top:2928px;left:0;width:1200px;height:322px;background:var(--grey);text-align:center}
.testimonials .kicker{margin-top:30px;font-size:16px;color:var(--ink);font-weight:600}
.testimonials h3{color:var(--purple);font-size:17px;font-weight:700}
.quote-mark{margin:34px auto 0;color:var(--silver);font-family:"Russo One",sans-serif;font-size:44px;line-height:30px}
.testimonials blockquote{font-size:13px;line-height:19px;width:520px;margin:8px auto 0}
.author{display:flex;align-items:center;justify-content:center;gap:10px;margin-top:34px;font-size:11px;color:var(--purple)}
.author i{width:38px;height:38px;border-radius:50%;background:#c9bdb3;display:block}
.arrow{position:absolute;top:150px}

/* tips */
.tips{position:absolute;top:3250px;left:0;width:1200px;height:468px;background:var(--dark)}
.tips h2{color:var(--white);text-align:center;font-size:25px;margin-top:40px}
.tips-grid{position:absolute;top:124px;left:246px;display:grid;grid-template-columns:repeat(3,240px);column-gap:34px;row-gap:40px}
.tip{display:flex;gap:14px;font-size:11px;line-height:15px;color:#9aa0a5;font-weight:600;min-height:60px}
.tip::before{content:"";flex:none;width:8px;height:8px;border-radius:50%;background:var(--purple);margin-top:4px}

/* footer */
.footer{position:absolute;top:3718px;left:0;width:1200px;height:300px;background:var(--ink);color:#777}
.footer .brand{position:absolute;top:44px;left:102px;font-size:46px;color:var(--white)}
.footer .brand .brand-dot{background:var(--white)}
.fbtn{position:absolute;left:106px;width:144px;height:34px;font-size:13px;color:var(--white);display:flex;align-items:center;justify-content:center;gap:8px;border-radius:3px;text-decoration:underline}
.fbtn.solid{top:108px;background:var(--purple)}
.fbtn.line{top:156px;border:1px solid var(--purple)}
.footer .social{position:absolute;top:218px;left:108px;color:var(--white)}
.divider{position:absolute;top:30px;width:1px;height:190px;background:#2a2a2a}
.news{position:absolute;top:60px;left:472px;width:250px}
.news h4{color:var(--purple);font-size:10px;font-weight:600}
.news .field{display:flex;margin-top:12px}
.news .field span{width:208px;height:48px;background:#f2f2f2;border-radius:3px 0 0 3px;font-size:10px;color:#aaa;padding:17px 24px}
.news .field b{width:52px;height:48px;background:var(--purple);color:var(--white);font-size:13px;text-align:center;line-height:48px;border-radius:0 3px 3px 0}
.news p{font-size:9px;line-height:13px;margin-top:10px}
.sitemap{position:absolute;top:56px;left:908px;width:220px}
.sitemap h4{color:var(--purple);font-size:10px;font-weight:600}
.sitemap ul{list-style:none;display:grid;grid-template-columns:110px 110px;row-gap:22px;margin-top:20px;font-size:10px;color:#bbb}
.copyright{position:absolute;bottom:12px;left:0;right:0;text-align:center;font-size:9px;color:#555}
.copyright b{color:#999}
</style>
</head>
<body>

<header class="hero">
  <div class="hero-photo" role="img" aria-label="Photo of a bed with soft rumpled sheets by a window"></div>
  <div class="brand"><span class="brand-dot"></span>Plimbo</div>
  <div class="social"><span></span><span></span><span></span></div>
  <p class="hero-copy">Play this audio in the background at a low to medium decibel level as you sleep. Other than the internet data used to stream, its free. Just click the play button you see to your left. The 33 minute track will automatically loop. Please use <em>at your own risk</em></p>
  <div class="play"><svg width="44" height="52" viewBox="0 0 44 52"><path d="M0 0 L44 26 L0 52 Z" fill="rgba(255,255,255,.7)"/></svg></div>
  <div class="dots"><span class="on"></span><span></span><span></span><span></span><span></span></div>
</header>

<nav class="nav">
  <div class="brand"><span class="brand-dot"></span>Plimbo</div>
  <ul>
    <li class="active">home</li><li>how it works</li><li>benefits</li><li>what to expect</li><li>testimonials</li><li>tips &amp; tricks</li><li>contact us</li>
  </ul>
  <div class="social"><span></span><span></span><span></span></div>
</nav>

<section class="how">
  <div class="how-text">
    <h2 class="heading">How it works</h2>
    <p>In a recent study scientists observed laying in a bed that is rocking back and forth can literally make you sleep sooner and deeper. For those who do not have a rocking bed, Plimbo is a white noise that oscillates in pitch to harness the calming and sedating effects of mundane repetition.</p>
    <p class="lead">Plimbo was created to answer these questions:</p>
    <p>- What is it about repetitive back and forth movement that makes it sedating?</p>
    <p>- Is physically rocking the only way to capture the effect?</p>
    <p>- Is it possible we don't necessarily need to be moving back and forth, we simply need to perceive back and forth movement?</p>
    <p>- Can seeing or hearing repetitive back and forth movement have the same or similar effect?</p>
    <p>- Isn't that how counting sheep works?</p>
  </div>
  <div class="how-photo" role="img" aria-label="Photo of a bedside table with an alarm clock next to pillows"></div>
</section>

<section class="benefits">
  <h2 class="heading">Proven benefits of plentiful rest</h2>
  <div class="grid">
    <div class="bubble" role="img" aria-label="Photo of a smiling couple"><b>better moods</b></div>
    <div class="bubble dim" role="img" aria-label="Photo of a person focused on work"><b>more focus</b></div>
    <div class="bubble mono" role="img" aria-label="Photo of people running"><b>more energy</b></div>
    <div class="bubble warm" role="img" aria-label="Photo of an elderly person in a hat"><b>longer life</b></div>
    <div class="bubble dim" role="img" aria-label="Photo of a couple in bed"><b>better sex</b></div>
    <div class="bubble" role="img" aria-label="Photo of a person looking relieved"><b>fewer mistakes</b></div>
    <div class="bubble mono" role="img" aria-label="Photo of pill blister packs"><b>less pain</b></div>
    <div class="bubble" role="img" aria-label="Photo of a smiling couple"><b>better moods</b></div>
    <div class="bubble dim" role="img" aria-label="Photo of a person focused on work"><b>more focus</b></div>
    <div class="bubble mono" role="img" aria-label="Photo of people running"><b>more energy</b></div>
    <div class="bubble warm" role="img" aria-label="Photo of an elderly person in a hat"><b>longer life</b></div>
    <div class="bubble dim" role="img" aria-label="Photo of a couple in bed"><b>better sex</b></div>
    <div class="bubble" role="img" aria-label="Photo of a person looking relieved"><b>fewer mistakes</b></div>
    <div class="bubble mono" role="img" aria-label="Photo of pill blister packs"><b>less pain</b></div>
    <div class="bubble" role="img" aria-label="Photo of a smiling couple"><b>better moods</b></div>
    <div class="bubble dim" role="img" aria-label="Photo of a person focused on work"><b>more focus</b></div>
    <div class="bubble mono" role="img" aria-label="Photo of people running"><b>more energy</b></div>
    <div class="bubble warm" role="img" aria-label="Photo of an elderly person in a hat"><b>longer life</b></div>
    <div class="bubble dim" role="img" aria-label="Photo of a couple in bed"><b>better sex</b></div>
    <div class="bubble" role="img" aria-label="Photo of a person looking relieved"><b>fewer mistakes</b></div>
    <div class="bubble mono" role="img" aria-label="Photo of pill blister packs"><b>less pain</b></div>
  </div>
</section>

<section class="download">
  <h2 class="heading">Want to own 10 continuous hours?</h2>
  <p>buy our <strong>10 hour</strong> continuous sleep music for just <strong>2.99$</strong></p>
  <div class="btn">DOWNLOAD (2.99$)</div>
</section>

<section class="expect">
  <div class="expect-photo" role="img" aria-label="Photo of a laptop showing the Plimbo site beside a speaker"></div>
  <div class="expect-text">
    <h2 class="heading">What to expect</h2>
    <p>With Plimbo playing in the background, we think you can expect to sleep a little bit sooner and a little bit deeper. But it isn't a tranquilizer. Don't expect to turn it on and to be asleep within 5 seconds. And don't expect to sleep so deep you'll only need 3 hours per night. We estimate you'll notice a 1 to 10% improvement on how much rest you currently extract from your time in bed.</p>
    <div class="btn">learn more</div>
  </div>
</section>

<section class="testimonials">
  <p class="kicker">people talk about us</p>
  <h3>see how their sleep got better with plimbo!</h3>
  <div class="quote-mark">"</div>
  <blockquote>"Lorem ipsum dolor sit amet, consectetur adipiscing elit. Morbi vitae accumsan metus. In lacus nunc, bibendum non accumsan quis, condimentum commodo justo.</blockquote>
  <div class="author"><i role="img" aria-label="Portrait of the reviewer"></i>DANA WHITFIELD / CEO PRESIDENT / DANA'S STUDIO</div>
  <svg class="arrow" style="left:74px" width="28" height="40" viewBox="0 0 28 40"><path d="M24 2 L4 20 L24 38" fill="none" stroke="#b9bcc0" stroke-width="6"/></svg>
  <svg class="arrow" style="left:1096px" width="28" height="40" viewBox="0 0 28 40"><path d="M4 2 L24 20 L4 38" fill="none" stroke="#b9bcc0" stroke-width="6"/></svg>
</section>

<section class="tips">
  <h2 class="heading">Tips &amp; tricks for a great fast sleep</h2>
  <div class="tips-grid">
    <div class="tip">Count the oscillations</div>
    <div class="tip">Play Plimbo through good-quality speakers if possible.</div>
    <div class="tip">Avoid afternoon or evening caffeine.</div>
    <div class="tip">Every ten oscillations take a very deep breath, hold it in for an entire cycle, and exhale very slowly.</div>
    <div class="tip">Sleep with your room temperature around 65 degrees farenheit and sleep in complete darkness.</div>
    <div class="tip">Avoid more than 1 or 2 alcoholic beverages.</div>
    <div class="tip">Envision something moving in sync with the oscillations.</div>
    <div class="tip">Go to bed at roughly the same time every night.</div>
    <div class="tip">Try stretching or yoga before bed; a relaxed body is a relaxed mind.</div>
  </div>
</section>

<footer class="footer">
  <div class="brand"><span class="brand-dot"></span>Plimbo</div>
  <div class="fbtn solid">go to player</div>
  <div class="fbtn line">buy 10 hours</div>
  <div class="social"><span></span><span></span><span></span></div>
  <div class="divider" style="left:372px"></div>
  <div class="divider" style="left:820px"></div>
  <div class="news">
    <h4>subscribe to our mailing list</h4>
    <div class="field"><span>your email address</span><b>GO</b></div>
    <p>* Don't worry, we don't spam. We will only provide information and news about our product.</p>
  </div>
  <div class="sitemap">
    <h4>main site map</h4>
    <ul><li>home</li><li>testimonials</li><li>how it works</li><li>tips &amp; tricks</li><li>benefits</li><li>contact us</li><li>what to expect</li></ul>
  </div>
  <p class="copyright">Copyright © 2015 <b>PLIMBO</b>. Use of this website constitutes acceptance of our <b>User Agreement</b> and <b>Privacy Policy</b>.</p>
</footer>

</body>
</html>
```